Pregnancy and Fertility Information Website

Hello Designers,
I need a website which provide tips and information about healthy and happy pregnancy. My website name is Lorvin medical.

The website should provide all the information needed throughout pregnancy and beyond ranging from pregnancy tracking tools and articles about common pregnancy concerns and what to expect during pregnancy,etc.
The details about first trimester, second trimester and third trimester should be highlighted in the website.

Top Navigation
Home, Fertility, Pregnancy basics, Articles, Tips and News

I'm looking for a simple and clean design which involves captivating images and colors but it shouldn't be crowded. The design must be professional and modern. An easy to navigate layout is a must.

Green, violet, blue and light yellow colors are my favorites but i'm open to other options.

Any questions. Kindly ask

Industry/Entity Type

Medical

```html
<!DOCTYPE html>
<html lang="en">
<head>
<meta charset="utf-8">
<title>Lorvin medical — Tips and News</title>
<link rel="stylesheet" href="https://fonts.googleapis.com/css2?family=Source+Sans+3:wght@400;600;700&display=swap">
<style>
  :root {
    --green: #62b94f;
    --green-dark: #2f6b1f;
    --text: #464646;
    --heading: #474747;
    --white: #ffffff;
    --news-from: #c9e3c3;
    --news-to: #a2d1de;
    --photo-light: #f2ece8;
    --photo-warm: #f4d4cf;
    --dot: #e6e6e6;
  }
  * { margin: 0; padding: 0; box-sizing: border-box; }
  html, body { width: 1200px; height: 676px; overflow: hidden; }
  body {
    position: relative;
    background: var(--white);
    font-family: "Source Sans 3", "Myriad Pro", sans-serif;
    color: var(--text);
  }

  /* Tips */
  .tips { position: absolute; left: 0; top: 0; width: 621px; height: 391px; background: var(--white); }
  .tips-title {
    position: absolute; left: 143px; top: 38px;
    display: flex; align-items: center; gap: 14px;
    color: var(--green); font-weight: 400; font-size: 41px; line-height: 1;
  }
  .tips-title svg { width: 32px; height: 32px; }
  .tips-list { position: absolute; left: 143px; top: 97px; list-style: none; }
  .tips-list li {
    position: relative; padding-left: 19.5px;
    font-size: 15px; line-height: 33.3px; color: var(--text);
  }
  .tips-list li::before {
    content: ""; position: absolute; left: 0; top: 12px;
    width: 10px; height: 10px; border-radius: 50%; background: var(--green);
  }

  .tips-photo {
    position: absolute; left: 621px; top: 0; width: 579px; height: 391px;
    background: linear-gradient(110deg, var(--photo-light) 0%, #f6f1ee 45%, var(--photo-warm) 70%, #ece6e1 100%);
  }

  /* News */
  .news {
    position: absolute; left: 0; top: 391px; width: 1200px; height: 285px;
    background: linear-gradient(90deg, var(--news-from) 0%, #bcdccb 35%, var(--news-to) 62%, var(--news-to) 100%);
  }
  .news-title {
    position: absolute; left: 532px; top: 42px;
    display: flex; align-items: center; gap: 11px;
    font-size: 42px; font-weight: 400; color: var(--heading); line-height: 1;
  }
  .news-title svg { width: 29px; height: 27px; }

  .news-date { position: absolute; left: 227px; top: 107px; width: 86px; text-align: center; color: var(--heading); }
  .news-date .day { display: block; font-size: 29px; line-height: 30px; font-weight: 400; letter-spacing: 0.5px; }
  .news-date .rule { display: block; height: 1px; background: var(--heading); margin: 5px 0 4px; }
  .news-date .year { display: block; font-size: 37px; line-height: 38px; font-weight: 700; }

  .news-item { position: absolute; left: 332px; top: 106px; width: 622px; }
  .news-item h3 { font-size: 20px; font-weight: 600; line-height: 24px; color: var(--heading); }
  .news-item p { font-size: 14.4px; line-height: 19px; text-align: justify; color: var(--text); }
  .read-more {
    display: inline-block; margin-top: 20px;
    font-size: 11px; color: var(--green-dark); text-decoration: none; text-transform: uppercase;
  }

  .slider-dots { position: absolute; left: 520px; top: 232px; display: flex; gap: 11.5px; list-style: none; }
  .slider-dots li { width: 14px; height: 14px; border-radius: 50%; background: var(--dot); }
  .slider-dots li.is-active { background: var(--green); }
</style>
</head>
<body>
  <section class="tips">
    <h2 class="tips-title">
      <svg viewBox="0 0 32 32" aria-hidden="true">
        <path d="M16 2.5a13.5 13.5 0 1 0 7 25l5.5 2.5-1.6-5.4A13.5 13.5 0 0 0 16 2.5z" fill="none" stroke="currentColor" stroke-width="2"/>
        <circle cx="16.5" cy="9.5" r="2" fill="currentColor"/>
        <path d="M14 14h3.5l-2 9h2.2" fill="none" stroke="currentColor" stroke-width="2.2" stroke-linecap="round" stroke-linejoin="round"/>
      </svg>
      Tips
    </h2>
    <ul class="tips-list">
      <li>Etiam ullamcorper augue quis ex consectetur commodo.</li>
      <li>Fusce vitae eros eget mauris cursus tempus a ut quam.</li>
      <li>Etiam maximus odio at elit bibendum rhoncus.</li>
      <li>Duis in ligula gravida, bibendum turpis in, aliquam erat.</li>
      <li>Vivamus in erat malesuada, laoreet ex at, volutpat leo.</li>
      <li>Phasellus gravida nibh quis purus consecteturipsum finibus.</li>
      <li>Aenean facilisis sem facilisis, tempus dui in, iaculis justo.</li>
    </ul>
  </section>

  <div class="tips-photo" role="img" aria-label="Photo of a pregnant woman in a pink top beside a kitchen counter with a bottle of milk, a banana, strawberries, a red apple and a bowl of muesli with fruit"></div>

  <section class="news">
    <h2 class="news-title">
      <svg viewBox="0 0 29 27" aria-hidden="true" fill="none" stroke="var(--heading)" stroke-width="1.8" stroke-linejoin="round">
        <path d="M2 9h6l12-7v21L8 16H2z"/>
        <path d="M5 16l3 9h4l-2-9"/>
        <path d="M24 8c2 1.5 2 7 0 8.5"/>
      </svg>
      News
    </h2>

    <div class="news-date">
      <span class="day">25 FEB</span>
      <span class="rule"></span>
      <span class="year">2017</span>
    </div>

    <article class="news-item">
      <h3>Mauris vestibulum vel libero sed aliquet</h3>
      <p>Sed urna dolor, mattis eu massa non, aliquam sollicitudin nulla. Suspendisse sagittis lorem nunc. Mauris elit quam, euismod quis ex sodales, luctus dignissim enim. Nam ultrices dui ut lectus tincidunt consectetur. Nunc malesuada congue augue, quis lobortis mi consectetur luctus ...</p>
      <a class="read-more" href="#">Read more.</a>
    </article>

    <ul class="slider-dots">
      <li></li>
      <li class="is-active"></li>
      <li></li>
      <li></li>
      <li></li>
      <li></li>
    </ul>
  </section>
</body>
</html>
```